Craft Beer and Sausage Bar Cluttered look

The Bar carries only local beers from Kegs and given as draft beers. The design needs to be dedicated towards the young crowd, and yes, we would like a more cluttered and different look. I have included the symbol and the logo to improve the idea. We will be having a 360 view of the locations, high end photos, and many images we can add into a galleries section. The main focus needs to be the initial vision that a user gets as soon as they look at the landing page.

Ive received several queries about one question and I'd like to clarify...

Just a psd for the home page will be fine, i have my own team that can convert it to a responsive html and into a site. and here are some more pics...
https://www.filecrate.example/sh/kq72lm9zt4r083x/BBtwqrfXoplaMNz-vuteQsLp?dl=0

Target Market(s)

21 to 40 year old crowd

Industry/Entity Type

Crowd

Number of Pages Required

1 page

Font styles to use
Other font styles liked:
• chalkboard and rough look, tattoo styles

Requirements
Must have
• Focus on Craft Beer and cluttered look, we will have many locations of the locations, already up to 3 locations and a food truck, and is growing another two locations in just another month., to show you the design of the truck, ive included that in the attached and its ONLY YO GIVE THE IDEA
Nice to have
• Something different, should portray the image of local brews are being served
• Some examples they liked...
• http://www.marlowetwins.example
• (Rebranded for Beer of course) http://www.pukanut.example
• http://www.brambleleaflounge.example/
• http://www.feine-kiste.example/
• http://fernlanehopyard.example/
• https://www.corntrader.example/
• http://theowlsperchbos.example/
Should not have
• No standard slider at the top, etc. should not look like a chain, nor family place. needs to be for the younger dating crowd

```html
<!DOCTYPE html>
<html lang="en">
<head>
<meta charset="utf-8">
<title>Ferro Hall — Craft Beer Company</title>
<link rel="stylesheet" href="https://fonts.googleapis.com/css2?family=Oswald:wght@400;500;700&family=Open+Sans:wght@400;700&display=swap">
<style>
:root{
  --red:#d12a2e;
  --red-dark:#b01f24;
  --orange:#f7941d;
  --orange-hot:#f15a24;
  --ink:#111111;
  --charcoal:#1c1c1c;
  --wood-dark:#2a1d14;
  --wood-mid:#4a3223;
  --white:#ffffff;
  --muted:#bdbdbd;
  --head:'Oswald',Impact,sans-serif;
  --body:'Open Sans',Arial,sans-serif;
}
*{margin:0;padding:0;box-sizing:border-box}
html,body{width:1200px;height:3212px;overflow:hidden;background:var(--ink)}
body{position:relative;font-family:var(--body);color:var(--white)}
.abs{position:absolute}
.photo{position:absolute;display:block}

/* hero */
.hero{left:0;top:0;width:1200px;height:670px;background:linear-gradient(160deg,#3a3530 0%,#6b5a48 35%,#2a2420 70%,#141210 100%)}
.hero-shade{left:0;top:0;width:1200px;height:670px;background:linear-gradient(90deg,rgba(0,0,0,.55),rgba(0,0,0,.1) 70%)}
.brand{left:40px;top:36px;font-family:var(--head);font-weight:700;font-size:34px;color:var(--white);display:flex;align-items:center;gap:10px;letter-spacing:.5px}
.brand-dot{width:18px;height:18px;background:var(--red)}
.nav{left:400px;top:52px;display:flex;gap:38px;font-family:var(--head);font-size:20px;font-weight:500;letter-spacing:.5px}
.nav a{color:var(--white);text-decoration:none}
.nav a.is-active{color:var(--orange)}
.hero-title{left:76px;top:336px;font-family:var(--head);font-weight:700;font-size:80px;line-height:1;color:var(--red)}
.hero-title span{color:var(--orange)}
.hero-sub{left:80px;top:432px;font-family:var(--head);font-weight:700;font-size:38px;line-height:1.2;text-transform:uppercase;width:800px}

/* brand band + menu */
.name-band{left:0;top:670px;width:640px;height:170px;background:var(--red);font-family:var(--head);font-weight:700;font-size:80px;display:flex;align-items:center;padding-left:60px}
.menu{left:0;top:840px;width:640px;height:950px;background:linear-gradient(180deg,var(--wood-mid),var(--wood-dark) 40%,#1a120c)}
.menu-title{position:absolute;left:0;width:640px;top:30px;text-align:center;font-family:var(--head);font-weight:700;font-size:84px;color:var(--orange)}
.menu-rule{position:absolute;left:60px;width:520px;top:150px;height:3px;background:var(--orange)}
.menu-list{position:absolute;left:60px;top:170px;width:520px;list-style:none}
.menu-list li{display:flex;justify-content:space-between;align-items:center;height:62px;border-bottom:1px solid rgba(255,255,255,.18);font-family:var(--head);font-size:19px;letter-spacing:.5px}
.menu-list .price{color:var(--red);font-weight:700;font-size:21px}
.menu-arrows{position:absolute;left:492px;top:866px;display:flex;gap:6px}
.menu-arrows span{width:36px;height:36px;background:var(--red);display:flex;align-items:center;justify-content:center}

/* right column */
.drinker{left:640px;top:670px;width:560px;height:580px;background:linear-gradient(135deg,#5a3c2a,#2b1c14 55%,#8a5a2a)}
.craft-title{left:680px;top:1060px;font-family:var(--head);font-weight:700;font-size:60px;color:var(--red)}
.craft-title span{color:var(--orange)}
.craft-sub{left:682px;top:1140px;width:480px;font-family:var(--head);font-size:22px;font-weight:500;line-height:1.35}
.snap-a{left:640px;top:1250px;width:280px;height:200px;background:linear-gradient(135deg,#c86a2a,#6a3a22)}
.snap-b{left:920px;top:1250px;width:280px;height:200px;background:linear-gradient(135deg,#3a3a3a,#8a7060)}
.link-bar{left:640px;top:1450px;width:560px;height:80px;background:var(--red);display:flex;justify-content:space-between;align-items:center;padding:0 16px;font-family:var(--head);font-weight:700;font-size:34px}
.link-bar small{font-size:13px;color:var(--orange);margin-left:8px}
.store{left:640px;top:1530px;width:560px;height:160px;background:linear-gradient(180deg,#9ab8d8,#d84a2a 55%,#5a2a1a)}
.about{left:640px;top:1690px;width:560px;height:100px;background:var(--ink);padding:14px 20px}
.about h3{font-family:var(--head);font-weight:700;font-size:34px;line-height:1}
.about h3 span{color:var(--red)}
.about p{font-size:13px;color:var(--muted);margin-top:6px}

/* come out */
.crowd{left:0;top:1790px;width:1200px;height:510px;background:linear-gradient(90deg,#4a3a2e,#7a6a5a 30%,#3a2e26 60%,#6a5a4a 85%,#2a2220)}
.play-box{left:230px;top:1930px;width:740px;height:280px;background:rgba(20,20,20,.8);text-align:center;padding:24px 40px}
.play-box h2{font-family:var(--head);font-weight:700;font-size:72px;line-height:1;color:var(--red)}
.play-box p{font-size:14px;line-height:1.7;margin-top:18px;color:#e6e6e6}

/* news */
.news-band{left:0;top:2300px;width:1200px;height:100px;background:var(--orange);text-align:center;font-family:var(--head);font-weight:700;font-size:70px;line-height:100px}
.news-grid{left:0;top:2400px;width:1200px;height:610px;display:grid;grid-template-columns:repeat(3,400px);grid-template-rows:310px 300px}
.news-img{width:400px;height:100%}
.news-card{background:var(--red);padding:28px 30px}
.news-card h4{font-family:var(--head);font-weight:700;font-size:30px;line-height:1.1}
.news-card p{font-size:13px;line-height:1.6;margin-top:16px}

/* footer */
.footer{left:0;top:3010px;width:1200px;height:202px;background:var(--charcoal);text-align:center}
.footer-nav{display:flex;justify-content:center;gap:56px;margin-top:40px;font-family:var(--head);font-size:14px;color:var(--muted)}
.copyright{font-size:12px;color:#888;margin-top:10px}
.social{display:flex;justify-content:center;gap:60px;margin-top:34px;font-family:var(--head);font-size:24px;color:#9a9a9a}
</style>
</head>
<body>

<div class="photo hero abs" role="img" aria-label="Photo of a busy bar with people raising glasses of draft beer"></div>
<div class="hero-shade abs"></div>
<div class="brand abs"><span class="brand-dot"></span>Ferro Hall</div>
<nav class="nav abs">
  <a class="is-active" href="#">HOME</a><a href="#">ABOUT US</a><a href="#">SERVICES</a><a href="#">PRODUCTS</a><a href="#">MENUS</a><a href="#">NEWS</a><a href="#">CONTACT US</a>
</nav>
<h1 class="hero-title abs">Craft beer <span>company</span></h1>
<p class="hero-sub abs">The bar carries only local beers from kegs and given as draft beers</p>

<div class="name-band abs">FERRO HALL</div>
<section class="menu abs">
  <h2 class="menu-title">MENU</h2>
  <div class="menu-rule"></div>
  <ul class="menu-list">
    <li>HOLLOW CREEK BLUEBERRY BRETT MINT<span class="price">$ 12.00</span></li>
    <li>HOLLOW CREEK BLUEBERRY BRETT MINT<span class="price">$ 12.00</span></li>
    <li>HOLLOW CREEK BLUEBERRY BRETT MINT<span class="price">$ 12.00</span></li>
    <li>HOLLOW CREEK BLUEBERRY BRETT MINT<span class="price">$ 12.00</span></li>
    <li>HOLLOW CREEK BLUEBERRY BRETT MINT<span class="price">$ 12.00</span></li>
    <li>HOLLOW CREEK BLUEBERRY BRETT MINT<span class="price">$ 12.00</span></li>
    <li>HOLLOW CREEK BLUEBERRY BRETT MINT<span class="price">$ 12.00</span></li>
    <li>HOLLOW CREEK BLUEBERRY BRETT MINT<span class="price">$ 12.00</span></li>
    <li>HOLLOW CREEK BLUEBERRY BRETT MINT<span class="price">$ 12.00</span></li>
    <li>HOLLOW CREEK BLUEBERRY BRETT MINT<span class="price">$ 12.00</span></li>
  </ul>
  <div class="menu-arrows">
    <span><svg width="14" height="14" viewBox="0 0 14 14"><path d="M10 1 L3 7 L10 13" fill="none" stroke="#fff" stroke-width="3"/></svg></span>
    <span><svg width="14" height="14" viewBox="0 0 14 14"><path d="M4 1 L11 7 L4 13" fill="none" stroke="#fff" stroke-width="3"/></svg></span>
  </div>
</section>

<div class="photo drinker" role="img" aria-label="Photo of a man drinking a glass of amber beer"></div>
<h2 class="craft-title abs">CRAFT<span>BIER</span></h2>
<p class="craft-sub abs">LOREM IPSUM IS SIMPLY DUMMY TEXT OF THE PRINTING AND TYPESETTING...</p>
<div class="photo snap-a" role="img" aria-label="Photo of sausages with mustard and beer"></div>
<div class="photo snap-b" role="img" aria-label="Photo of a row of beer tap handles"></div>
<div class="link-bar abs"><div>ADVENTURE<small>READ MORE</small></div><div>OUR STORE<small>READ MORE</small></div></div>
<div class="photo store" role="img" aria-label="Photo of the bar storefront with red awning"></div>
<div class="about abs"><h3>ABOUT<span>FERRO HALL</span></h3><p>Local kegs, poured fresh every single night</p></div>

<div class="photo crowd" role="img" aria-label="Photo of a group of young friends smiling in the bar"></div>
<div class="play-box abs">
  <h2>COME OUT TO PLAY</h2>
  <p>Fresh kegs from the brewers down the road, poured cold at every tap we run. Grab your crew, claim a long table, try a flight of something new and stay for the sausages, the music and whoever walks in next. Tonight the first round starts early.</p>
</div>

<div class="news-band abs">LATEST NEWS</div>
<section class="news-grid abs">
  <div class="photo news-img" style="position:static;background:linear-gradient(135deg,#8a1a1a,#2a1a1a)" role="img" aria-label="Photo of the food truck at night"></div>
  <article class="news-card"><h4>LOREM IPSUM IS SIMPLY DUMMY</h4><p>Our third taproom opens next month with twenty local lines, a brand new grill and the food truck parked right outside. Come early for the opening night pours and music.</p></article>
  <div class="photo news-img" style="position:static;background:linear-gradient(135deg,#2a2a3a,#c8903a 60%,#3a2a20)" role="img" aria-label="Photo of a crowded beer hall under string lights"></div>
  <article class="news-card"><h4>LOREM IPSUM IS SIMPLY DUMMY</h4><p>Our third taproom opens next month with twenty local lines, a brand new grill and the food truck parked right outside. Come early for the opening night pours and music.</p></article>
  <div class="photo news-img" style="position:static;background:linear-gradient(135deg,#6a4a2a,#c8a060 50%,#4a3020)" role="img" aria-label="Photo of a tray of fries and beer tasting glasses"></div>
  <article class="news-card"><h4>LOREM IPSUM IS SIMPLY DUMMY</h4><p>Our third taproom opens next month with twenty local lines, a brand new grill and the food truck parked right outside. Come early for the opening night pours and music.</p></article>
</section>

<footer class="footer abs">
  <div class="footer-nav"><span>HOME</span><span>ABOUT US</span><span>SERVICES</span><span>PRODUCTS</span><span>MENUS</span><span>NEWS</span><span>CONTACT</span></div>
  <p class="copyright">© 2024 Ferro Hall. All rights reserved.</p>
  <div class="social"><span>Facetome</span><span>Chirper</span><span>Pinboard Co</span><span>Snapgram</span></div>
</footer>

</body>
</html>
```